Update Old OR create new Website

Current Website is looking a bit old, I did this one a few years back.

Would like a fresh new look, current website sitepress theme is " the Vanta theme" from plumcrate and I just purchased this theme - "bravlo" also from plumcrate, I quite like the look of - http://bravlo.quorvex-skins.com/tech-business/ and if we could get somthing simlar would be great.

current website is at http://www.hle.com.au, have been playing around with the slider that i like.

I have said 5 pages to be designed but really it is just a 5 page website where most pages will look the same.

Any questions please let me know

Target Market(s)

Business

Coding

Coded - Design and coding required

Number of Pages Required

5+ page

Font styles to use
Sans Serif

Colors
33a6d7
0292cd
ffffff
0255a3

Requirements
Must have
• Device compatibility - pc, tablet, phone
Nice to have
• video
Should not have
• vunerabilities. Must also use images that will expire or disappear, ie must be uploaded to site not links to elsewhere.

```html
<!DOCTYPE html>
<html lang="en">
<head>
<meta charset="utf-8">
<title>Corvant</title>
<link href="https://fonts.googleapis.com/css2?family=Roboto:wght@300;400;500;700&display=swap" rel="stylesheet">
<style>
:root{
  --navy:#0255a3;
  --blue:#0292cd;
  --sky:#33a6d7;
  --white:#ffffff;
  --ink:#333333;
  --muted:#666666;
  --line:#e3e3e3;
  --band:#ececec;
  --dark:#2d2d2d;
  --disc:#4a4a4a;
}
*{margin:0;padding:0;box-sizing:border-box}
html,body{width:1200px;height:2736px;overflow:hidden}
body{font-family:'Roboto',Arial,sans-serif;color:var(--ink);background:var(--white);position:relative}
.abs{position:absolute}

/* top bar */
.topbar{left:0;top:0;width:1200px;height:37px;background:var(--navy);color:var(--white)}
.social{left:160px;top:6px;display:flex;gap:7px}
.social span{width:24px;height:24px;border-radius:50%;background:var(--white);display:block}
.contact-item{top:6px;display:flex;align-items:center;gap:10px;font-size:10px;line-height:12px;text-transform:uppercase}
.contact-item b{font-weight:400;text-transform:none;font-size:11px}

/* header */
.header{left:0;top:37px;width:1200px;height:76px;background:var(--white);border-bottom:1px solid var(--line)}
.brand{left:160px;top:22px;display:flex;align-items:center;gap:10px}
.brand-mark{width:32px;height:32px;background:var(--sky)}
.brand-name{font-size:22px;font-weight:500;color:var(--ink);line-height:1}
.nav{left:428px;top:27px;display:flex}
.nav a{font-size:11px;color:#555;text-decoration:none;padding:7px 10px;letter-spacing:.5px;white-space:nowrap}
.nav a.active{background:var(--sky);color:var(--white)}
.search{left:1012px;top:27px;width:26px;height:26px;background:var(--navy);display:flex;align-items:center;justify-content:center}

/* hero */
.hero{left:0;top:113px;width:1200px;height:540px;background:radial-gradient(ellipse at 50% 55%,#1d6fb2 0%,#0d3e75 35%,#061c3a 75%,#030d1d 100%)}
.arrow{top:260px;width:52px;height:26px;border:2px solid var(--white);border-radius:13px;display:flex;align-items:center;justify-content:center}

/* section titles */
.sec-title{left:0;width:1200px;display:flex;justify-content:center;align-items:center;gap:14px;color:var(--blue);font-size:19px;font-weight:500;letter-spacing:1.5px}
.sec-title i{display:block;width:46px;height:2px;background:var(--blue);position:relative}
.sec-title i::before{content:"";position:absolute;top:-3px;width:8px;height:8px;border-radius:50%;background:var(--blue)}
.sec-title i.l::before{left:0}
.sec-title i.r::before{right:0}

/* about */
.about-visual{left:164px;top:757px;width:292px;height:319px;border-radius:8px;background:radial-gradient(circle at 45% 35%,#6ea6e8 0%,#3f7fd6 35%,#e9eef5 70%,#ffffff 100%)}
.about-copy{left:562px;top:760px;width:490px}
.about-copy h2{font-size:19px;font-weight:300;line-height:26px;color:#444;margin-bottom:16px}
.about-copy li{list-style:none;position:relative;padding-left:25px;font-size:11px;line-height:16px;color:var(--muted);margin-bottom:12px}
.about-copy li::before{content:"";position:absolute;left:2px;top:3px;width:9px;height:9px;border-radius:50%;border:2px solid var(--blue)}

/* services */
.card{width:278px;height:130px;border:1px solid var(--line);background:var(--white)}
.card.featured{background:var(--sky);border-color:var(--sky);color:var(--white)}
.card svg{position:absolute;left:14px;top:34px}
.card h3{position:absolute;left:104px;top:20px;font-size:13px;font-weight:500;letter-spacing:1.5px;white-space:nowrap}
.card p{position:absolute;left:104px;top:44px;width:162px;font-size:11px;line-height:16px}
.card .more{position:absolute;left:104px;top:90px;border:1px solid var(--sky);color:var(--sky);font-size:9px;padding:5px 9px;letter-spacing:.5px}
.card.featured .more{border-color:var(--white);color:var(--white)}

/* process */
.process{left:0;top:1578px;width:1200px;height:297px;background:var(--band)}
.step{width:160px;text-align:center}
.step .disc{width:132px;height:132px;margin:0 auto;border-radius:50%;background:var(--disc);border:6px solid #dcdcdc;display:flex;align-items:center;justify-content:center}
.step.on .disc{background:var(--sky)}
.step .label{margin-top:18px;font-size:14px;font-weight:500;letter-spacing:1.5px;color:#444}
.step.on .label,.step.blue .label{color:var(--sky)}
.dash{top:1713px;height:0;border-top:2px dashed #777}

/* testimonial */
.vert{left:372px;top:2012px;transform-origin:left top;transform:rotate(-90deg) translateX(-180px);font-size:16px;letter-spacing:5px;color:#ccc;width:180px}
.vline{left:436px;top:2010px;width:1px;height:184px;background:var(--line)}
.avatar{left:479px;top:2013px;width:64px;height:64px;border-radius:50%;background:linear-gradient(#c9a27c,#8a6449)}
.quote{left:474px;top:2090px;width:500px;font-size:11px;line-height:20px;color:var(--muted)}
.who{left:474px;top:2158px;font-size:15px;color:#333}
.role{left:474px;top:2180px;font-size:10px;color:var(--muted)}

/* clients */
.clients{left:0;top:2271px;width:1200px;height:191px;background:var(--sky)}
.badge{top:78px;width:96px;height:36px;border-radius:4px;background:rgba(255,255,255,.85)}

/* footer */
.footer{left:0;top:2462px;width:1200px;height:274px;background:var(--dark);color:#bbb}
.foot-brand{left:160px;top:26px;display:flex;align-items:center;gap:10px}
.foot-brand .brand-name{color:#ddd}
.foot-about{left:160px;top:110px;width:200px;font-size:11px;line-height:17px;color:#bbb}
.foot-col{top:44px}
.foot-col h4{font-size:12px;font-weight:500;color:var(--white);letter-spacing:.5px;padding-bottom:6px;position:relative}
.foot-col h4::after{content:"";position:absolute;left:0;bottom:0;width:22px;height:2px;background:var(--sky)}
.foot-col ul{list-style:none;margin-top:30px}
.foot-col li{font-size:11px;line-height:14px;margin-bottom:11px;padding-left:28px;position:relative}
.foot-col li::before{content:"";position:absolute;left:2px;top:4px;width:6px;height:6px;border-radius:50%;background:#ddd}
.reach li::before{display:none}
.reach li svg{position:absolute;left:0;top:1px}
.foot-rule{left:160px;top:216px;width:880px;height:1px;background:#444}
.copy{left:0;top:238px;width:1200px;text-align:center;font-size:10px;color:#999}
</style>
</head>
<body>

<div class="abs topbar">
  <div class="abs social"><span></span><span></span><span></span><span></span></div>
  <div class="abs contact-item" style="left:656px">
    <svg width="20" height="20" viewBox="0 0 24 24"><path d="M6 3l3 0 2 5-2 1.5a11 11 0 0 0 5.5 5.5L16 13l5 2v3a2 2 0 0 1-2 2A16 16 0 0 1 4 5a2 2 0 0 1 2-2z" fill="none" stroke="#fff" stroke-width="1.6"/></svg>
    <div>Call us at<br><b>1300 482 615</b></div>
  </div>
  <div class="abs contact-item" style="left:782px">
    <svg width="22" height="16" viewBox="0 0 22 16"><rect x="1" y="1" width="20" height="14" fill="none" stroke="#fff" stroke-width="1.4"/><path d="M1 1l10 8 10-8" fill="none" stroke="#fff" stroke-width="1.4"/></svg>
    <div>Mail us at<br><b>info@hle.com.au</b></div>
  </div>
  <div class="abs contact-item" style="left:918px">
    <svg width="16" height="22" viewBox="0 0 16 22"><path d="M8 1a7 7 0 0 1 7 7c0 5-7 13-7 13S1 13 1 8a7 7 0 0 1 7-7z" fill="none" stroke="#fff" stroke-width="1.4"/><circle cx="8" cy="8" r="2.5" fill="#fff"/></svg>
    <div style="text-transform:none"><b>14b 2210 Harbour Rd,<br>Lower Elm Ridge</b></div>
  </div>
</div>

<header class="abs header">
  <div class="abs brand">
    <div class="brand-mark"></div>
    <div class="brand-name">Corvant</div>
  </div>
  <nav class="abs nav">
    <a class="active">HOME</a><a>SERVERS</a><a>NETWORKS</a><a>MANAGED IT</a><a>WEB</a><a>APP'S</a><a>INTERNET</a><a>CONTACT US</a>
  </nav>
  <div class="abs search"><svg width="14" height="14" viewBox="0 0 14 14"><circle cx="6" cy="6" r="4.2" fill="none" stroke="#fff" stroke-width="2"/><path d="M9 9l4 4" stroke="#fff" stroke-width="2"/></svg></div>
</header>

<section class="abs hero" role="img" aria-label="Data centre corridor with glowing blue server racks and a network overlay">
  <div class="abs arrow" style="left:12px"><svg width="16" height="12" viewBox="0 0 16 12"><path d="M15 6H2M6 1L1 6l5 5" fill="none" stroke="#fff" stroke-width="2.4"/></svg></div>
  <div class="abs arrow" style="left:1136px"><svg width="16" height="12" viewBox="0 0 16 12"><path d="M1 6h13M10 1l5 5-5 5" fill="none" stroke="#fff" stroke-width="2.4"/></svg></div>
  <svg class="abs" style="left:568px;top:244px" width="64" height="64" viewBox="0 0 64 64"><circle cx="32" cy="32" r="29" fill="rgba(0,0,0,.25)" stroke="#fff" stroke-width="3"/><path d="M25 19l20 13-20 13z" fill="none" stroke="#fff" stroke-width="3" stroke-linejoin="round"/></svg>
</section>

<div class="abs sec-title" style="top:694px"><i class="l"></i>WHO WE ARE<i class="r"></i></div>
<div class="abs about-visual" role="img" aria-label="Hand holding a smartphone with a blue bar chart rising from the screen"></div>
<div class="abs about-copy">
  <h2>What would it take for your information systems to actually improve the performance of your organisation?</h2>
  <ul>
    <li>Through Corvant, companies outsource all the expertise they need to secure their systems and optimise the output of their people and IT resources – without the expense of maintaining large internal IT departments.</li>
    <li>With a decade of experience, Corvant understands the challenges faced by SMEs. So when we design and build networks, support solutions, hardware and software there's room for growth, change and mobility.</li>
    <li>Corvant staff are not just short-term problem solvers – they are advanced systems designers and proactive thinkers who work closely with clients on issue detection and prevention. And, when problems do arise Corvant literally does whatever it takes to get clients back on track.</li>
    <li>It's this attitude that means Corvant enjoys long-term relationships with its clients.</li>
  </ul>
</div>

<div class="abs sec-title" style="top:1117px"><i class="l"></i>OUR BEST SERVICES<i class="r"></i></div>

<div class="abs card" style="left:160px;top:1187px">
  <svg width="74" height="70" viewBox="0 0 74 70"><path d="M10 60L46 24M40 14a12 12 0 0 1 16-4l-8 8 4 6 8-4a12 12 0 0 1-16 14M12 10l14 14M8 14l6-6M28 40l24 22 6-6-22-24" fill="none" stroke="#444" stroke-width="4" stroke-linecap="round"/></svg>
  <h3>MANAGED IT</h3><p>Lorem Ipsum is simply dummy of the printing and typesetting.</p><span class="more">READ MORE +</span>
</div>
<div class="abs card featured" style="left:460px;top:1187px">
  <svg width="80" height="70" viewBox="0 0 80 70"><path d="M18 56a14 14 0 0 1 0-28 20 20 0 0 1 38-6 16 16 0 0 1 6 34z" fill="none" stroke="#fff" stroke-width="3.5"/><path d="M40 30l12 4v10c0 7-5 11-12 14-7-3-12-7-12-14V34z" fill="#fff"/></svg>
  <h3>PRIVATE CLOUD</h3><p>Lorem Ipsum is simply dummy of the printing and typesetting.</p><span class="more">READ MORE +</span>
</div>
<div class="abs card" style="left:759px;top:1187px">
  <svg width="74" height="70" viewBox="0 0 74 70"><g fill="none" stroke="#444" stroke-width="3"><rect x="8" y="6" width="58" height="16"/><rect x="8" y="27" width="58" height="16"/><rect x="8" y="48" width="58" height="16"/></g><g fill="#444"><rect x="14" y="12" width="26" height="4"/><rect x="14" y="33" width="26" height="4"/><rect x="14" y="54" width="26" height="4"/><circle cx="58" cy="14" r="3"/><circle cx="58" cy="35" r="3"/><circle cx="58" cy="56" r="3"/></g></svg>
  <h3>SERVERS</h3><p>Lorem Ipsum is simply dummy of the printing and typesetting.</p><span class="more">READ MORE +</span>
</div>
<div class="abs card" style="left:160px;top:1339px">
  <svg width="74" height="70" viewBox="0 0 74 70"><g fill="none" stroke="#444" stroke-width="3"><circle cx="37" cy="35" r="30"/><ellipse cx="37" cy="35" rx="13" ry="30"/><path d="M7 35h60M12 20h50M12 50h50M37 5v60"/></g></svg>
  <h3>WEB SERVICES</h3><p>Lorem Ipsum is simply dummy of the printing and typesetting.</p><span class="more">READ MORE +</span>
</div>
<div class="abs card" style="left:460px;top:1339px">
  <svg width="74" height="70" viewBox="0 0 74 70"><g fill="none" stroke="#444" stroke-width="3"><rect x="6" y="4" width="62" height="62" rx="8" stroke-dasharray="4 3"/><circle cx="37" cy="35" r="20"/><path d="M23 21l28 28M51 21L23 49"/></g></svg>
  <h3>APPS</h3><p>Lorem Ipsum is simply dummy of the printing and typesetting.</p><span class="more">READ MORE +</span>
</div>
<div class="abs card" style="left:759px;top:1339px">
  <svg width="74" height="70" viewBox="0 0 74 70"><g fill="none" stroke="#444" stroke-width="6" stroke-linecap="round"><path d="M6 24a44 44 0 0 1 62 0M16 36a30 30 0 0 1 42 0M26 47a16 16 0 0 1 22 0"/></g><circle cx="37" cy="58" r="5" fill="#444"/></svg>
  <h3>INTERNET SOLUTIONS</h3><p>Lorem Ipsum is simply dummy of the printing and typesetting.</p><span class="more">READ MORE +</span>
</div>

<div class="abs sec-title" style="top:1518px"><i class="l"></i>HOW IT WORKS<i class="r"></i></div>
<div class="abs process"></div>
<div class="abs dash" style="left:290px;width:120px"></div>
<div class="abs dash" style="left:542px;width:120px"></div>
<div class="abs dash" style="left:794px;width:116px"></div>
<div class="abs step" style="left:144px;top:1648px">
  <div class="disc"><svg width="66" height="60" viewBox="0 0 66 60"><rect x="4" y="8" width="50" height="34" fill="none" stroke="#fff" stroke-width="3"/><path d="M22 42l-4 12h22l-4-12M14 54h30" stroke="#fff" stroke-width="3" fill="none"/><path d="M28 34l30-30 5 5-30 30-7 2z" fill="#fff"/></svg></div>
  <div class="label">DESIGN</div>
</div>
<div class="abs step on" style="left:396px;top:1648px">
  <div class="disc"><svg width="66" height="60" viewBox="0 0 66 60"><rect x="4" y="14" width="48" height="32" fill="none" stroke="#fff" stroke-width="3"/><path d="M20 46l-3 10h22l-3-10" stroke="#fff" stroke-width="3" fill="none"/><circle cx="46" cy="16" r="12" fill="#fff"/><circle cx="46" cy="16" r="5" fill="#33a6d7"/></svg></div>
  <div class="label">DEVELOPMENT</div>
</div>
<div class="abs step blue" style="left:648px;top:1648px">
  <div class="disc"><svg width="60" height="62" viewBox="0 0 60 62"><rect x="12" y="6" width="40" height="50" fill="none" stroke="#fff" stroke-width="3"/><rect x="24" y="2" width="16" height="8" fill="#fff"/><path d="M22 30l8 8 14-16" fill="none" stroke="#fff" stroke-width="4"/><circle cx="12" cy="50" r="8" fill="#fff"/><circle cx="12" cy="50" r="3" fill="#4a4a4a"/></svg></div>
  <div class="label">TESTING</div>
</div>
<div class="abs step" style="left:896px;top:1648px">
  <div class="disc"><svg width="50" height="64" viewBox="0 0 50 64"><path d="M25 2c10 10 12 24 8 40H17C13 26 15 12 25 2z" fill="#fff"/><circle cx="25" cy="22" r="5" fill="#4a4a4a"/><path d="M15 32L6 46h10zM35 32l9 14H34z" fill="#fff"/><path d="M20 46h10l-5 14z" fill="#fff"/></svg></div>
  <div class="label">LAUNCH</div>
</div>

<div class="abs sec-title" style="top:1918px"><i class="l"></i>CLIENT SPEAK<i class="r"></i></div>
<div class="abs vert">TESTIMONIALS</div>
<div class="abs vline"></div>
<div class="abs avatar" role="img" aria-label="Client portrait photo"></div>
<p class="abs quote">Lorem ipsum dolor sit amet, consectetuer adipiscing elit, sed diam nonummy nibh euismod tincidunt ut laoreet dolore magna, Lorem ipsum dolor sit amet, consectetuer adipiscing elit, sed diam nonummy nibh euismod tincidunt ut laoreet dolore magna</p>
<div class="abs who">Marcus Reed</div>
<div class="abs role">CEO</div>

<section class="abs clients" aria-label="Client badges">
  <div class="abs badge" style="left:167px"></div>
  <div class="abs badge" style="left:361px"></div>
  <div class="abs badge" style="left:552px"></div>
  <div class="abs badge" style="left:747px"></div>
  <div class="abs badge" style="left:937px"></div>
</section>

<footer class="abs footer">
  <div class="abs foot-brand">
    <div class="brand-mark"></div>
    <div class="brand-name">Corvant</div>
  </div>
  <p class="abs foot-about">There are many variations of passages of Lorem Ipsum available, but the majority have suffered alteration in some form, by injected humour, or randomised words which don't look even slightly believable.</p>
  <div class="abs foot-col" style="left:388px"><h4>INFORMATION</h4><ul><li>Home</li><li>Server</li><li>Networks</li><li>Managed IT</li></ul></div>
  <div class="abs foot-col" style="left:611px"><h4>MY ACCOUNT</h4><ul><li>Web</li><li>App's</li><li>Internet</li><li>Contact</li></ul></div>
  <div class="abs foot-col reach" style="left:837px"><h4>GET IN TOUCH</h4><ul>
    <li style="width:230px"><svg width="10" height="14" viewBox="0 0 10 14"><path d="M5 0a5 5 0 0 1 5 5c0 4-5 9-5 9S0 9 0 5a5 5 0 0 1 5-5z" fill="#ddd"/></svg>There are many variations of passages of Lorem Ipsum available</li>
    <li><svg width="12" height="12" viewBox="0 0 24 24"><path d="M6 3l3 0 2 5-2 1.5a11 11 0 0 0 5.5 5.5L16 13l5 2v3a2 2 0 0 1-2 2A16 16 0 0 1 4 5a2 2 0 0 1 2-2z" fill="#ddd"/></svg>1300 482 615</li>
    <li><svg width="13" height="10" viewBox="0 0 22 16"><rect x="1" y="1" width="20" height="14" fill="none" stroke="#ddd" stroke-width="2"/><path d="M1 1l10 8 10-8" fill="none" stroke="#ddd" stroke-width="2"/></svg>info@hle.com.au</li>
  </ul></div>
  <div class="abs foot-rule"></div>
  <div class="abs copy">Copyright © 2017 hle.com.au. All rights reserved.</div>
</footer>

</body>
</html>
```